IT-support company web-site design

We need to re-design out site for existing clients and for the future promotions. Site needs to be attractive with intuitive interface. We need to keep our logo and colors but any reshuffles can be made. I provide the working site and re-made version, which we do nt like. It has to be more bright and clear. All the blocks have to be divided and look like logic and structured. PLease find the addresses to work with below.
The "real" one https://qorbil.com
The version http://tomuski.net/Qorbil/
If you have any с

Industry/Entity Type

It Company

Number of Pages Required

5+ page

Font styles to use
Sans Serif

Colors
9bcb3c

Requirements
Must have
• Our LOGO and our colors (green palette). We d like to make our services blocks as the main things. We need to have our images and slogans as there are extremely important advantages of our company.
Nice to have
• Original and modern view of the site.
Should not have
• unpredictable and @surprising@, hard- definable buttons and ways

```html
<!DOCTYPE html>
<html lang="en">
<head>
<meta charset="utf-8">
<title>Qorbil — Managed IT Services</title>
<link href="https://fonts.googleapis.com/css2?family=Raleway:wght@400;500;600;700;800&family=Open+Sans:wght@400;600;700&display=swap" rel="stylesheet">
<style>
:root{
  --green:#5fc796;
  --lime:#9bcb3c;
  --mint:#8fdcb4;
  --text:#4a4a4a;
  --muted:#8a8a8a;
  --line:#e6e6e6;
  --dark:#232323;
  --white:#ffffff;
  --grad:linear-gradient(90deg,#9bcb3c 0%,#6fd3a3 60%,#8fe0c0 100%);
}
*{box-sizing:border-box;margin:0;padding:0}
html,body{width:1200px;height:3448px;overflow:hidden;background:var(--white)}
body{position:relative;font-family:"Open Sans",sans-serif;color:var(--text)}
.abs{position:absolute}
h1,h2,h3,h4{font-family:"Raleway",sans-serif}

/* header / hero */
.hero{left:0;top:0;width:1200px;height:563px;background:linear-gradient(135deg,#1d2a33 0%,#2f3f4a 35%,#233240 60%,#16222b 100%)}
.hero-photo{position:absolute;inset:0;background:
  repeating-linear-gradient(90deg,rgba(70,110,170,.18) 0 6px,transparent 6px 40px),
  linear-gradient(180deg,rgba(0,0,0,.1),rgba(0,0,0,.35))}
.logo{left:150px;top:14px;display:flex;align-items:center;gap:8px;color:var(--white);font-family:"Raleway",sans-serif;font-weight:700;font-size:26px;letter-spacing:1px}
.logo .dot{width:14px;height:14px;border-radius:50%;background:var(--lime)}
.nav{left:460px;top:0;width:740px;height:54px;background:var(--grad);clip-path:polygon(6% 0,100% 0,100% 100%,0 100%);display:flex;align-items:center;gap:34px;padding-left:78px;font-size:12px;color:var(--white);font-weight:600}
.nav .active{color:#fff7a8}
.nav .login{margin-left:10px;border:2px solid var(--white);border-radius:14px;padding:3px 34px;font-weight:700}
.hero-title{left:150px;top:198px;font-size:39px;font-weight:800;color:var(--white);letter-spacing:.5px}
.hero-title span{color:var(--green)}
.hero-copy{left:150px;top:250px;width:440px;color:var(--white);font-size:17px;line-height:30px}
.btn{display:inline-block;border-radius:22px;font-size:12px;font-weight:700;text-transform:uppercase;text-align:center}
.btn-fill{background:var(--grad);color:var(--white)}
.btn-ghost{border:2px solid var(--white);color:var(--white)}
.hero-cta{left:150px;top:363px;width:142px;height:40px;line-height:40px}
.hero-more{left:303px;top:363px;width:142px;height:40px;line-height:36px}
.slide-dots{left:1022px;top:276px;display:flex;flex-direction:column;gap:6px}
.slide-dots i{width:12px;height:12px;border-radius:50%;border:2px solid var(--white)}
.slide-dots i.on{background:var(--white)}
.scroll-down{left:588px;top:551px;width:24px;height:24px;border-radius:50%;background:var(--white)}

/* section heads */
.section-title{left:0;width:1200px;text-align:center;color:var(--green);font-size:32px;font-weight:500}
.section-sub{left:0;width:1200px;text-align:center;color:var(--muted);font-size:11px}

/* services */
.card{width:272px;height:327px;background:var(--white);box-shadow:0 4px 16px rgba(0,0,0,.12);border-top:4px solid var(--green);text-align:center}
.card .ph{height:146px}
.card h3{font-family:"Open Sans",sans-serif;font-size:14px;font-weight:400;color:#333;margin:16px 22px 10px;line-height:19px}
.card p{font-size:10px;line-height:18px;color:var(--muted);margin:0 26px}
.card .more{position:absolute;bottom:20px;left:0;width:100%;color:var(--green);font-size:10px;font-weight:700}
.divider{left:150px;top:1501px;width:900px;height:1px;background:var(--line)}

/* testimonials */
.quote{width:374px;height:184px;background:var(--white);border-radius:10px;box-shadow:0 4px 18px rgba(0,0,0,.12);padding:22px 28px}
.avatar{width:40px;height:40px;border-radius:50%}
.quote h4{font-size:15px;font-weight:700;color:#222;margin-bottom:8px;padding-bottom:8px;border-bottom:1px solid var(--line)}
.quote p{font-size:10px;line-height:20px;color:var(--muted)}
.quote .who{position:absolute;left:28px;bottom:14px;font-size:10px;line-height:14px;color:#222}
.quote .who b{color:var(--green);font-weight:600;display:block}
.fade{left:1040px;top:1680px;width:160px;height:215px;background:linear-gradient(90deg,rgba(255,255,255,.35),rgba(255,255,255,.85))}
.q-dots{left:578px;top:1964px;display:flex;align-items:center;gap:8px}
.q-dots i{width:6px;height:6px;border-radius:50%;background:#ccc}
.q-dots i.on{width:22px;height:22px;background:var(--mint)}

/* cost */
.cost{left:0;top:2062px;width:1200px;height:411px;border-top:1px solid var(--line);border-bottom:1px solid var(--line)}
.cost-photo{left:600px;top:2062px;width:600px;height:411px;background:linear-gradient(135deg,#2b3a36 0%,#3f6b58 45%,#7ed6a8 100%)}
.cost-title{left:150px;top:2110px;color:var(--green);font-size:25px;font-weight:600}
.cost-copy{left:150px;top:2158px;width:400px;font-size:10.5px;line-height:26px;color:var(--muted)}
.cost-copy span{color:var(--lime)}
.cost-copy .rm{color:var(--lime);font-weight:600}
.cost-btn{left:150px;top:2387px;width:120px;height:34px;line-height:34px;font-size:11px}

/* partners */
.partners{left:150px;top:2653px;width:900px;height:152px;border:1px solid #ddd;display:grid;grid-template-columns:repeat(3,1fr);grid-template-rows:1fr 1fr}
.partners div{border-right:1px solid #ddd;border-bottom:1px solid #ddd;display:flex;align-items:center;justify-content:center;gap:8px;font-family:"Raleway",sans-serif;font-weight:700;font-size:18px;color:#2f6f8f}
.partners div:nth-child(3n){border-right:none}
.partners div:nth-child(n+4){border-bottom:none}
.partners .sq{width:14px;height:14px;background:var(--green)}

/* newsletter */
.ask{left:0;top:2872px;width:1200px;text-align:center;color:var(--green);font-size:16px;letter-spacing:1px;font-weight:600;font-family:"Raleway",sans-serif}
.subscribe{left:405px;top:2931px;width:338px;height:34px;display:flex;border-radius:17px;overflow:hidden;box-shadow:0 2px 8px rgba(0,0,0,.1)}
.subscribe .field{flex:1;padding-left:22px;font-size:10px;line-height:34px;color:#555;background:var(--white)}
.subscribe .send{width:104px;background:var(--grad);color:var(--white);font-size:11px;line-height:34px;text-align:center}

/* footer */
.footer{left:0;top:3039px;width:1200px;height:352px;background:var(--dark)}
.fcol{top:3098px;color:var(--white)}
.fcol h4{font-size:14px;font-weight:700;margin-bottom:4px}
.fcol .rule{width:34px;border-top:2px dotted #777;margin-bottom:28px}
.fcol ul{list-style:none;font-size:11px;font-weight:700;line-height:25px}
.flogo{display:flex;align-items:center;gap:8px;font-family:"Raleway",sans-serif;font-weight:700;font-size:20px;margin-bottom:14px}
.flogo .dot{width:12px;height:12px;border-radius:50%;background:var(--lime)}
.ftag{font-size:11px;font-weight:700;line-height:26px;width:150px}
.socials{display:grid;grid-template-columns:repeat(3,20px);gap:10px 12px;margin-top:18px}
.socials i{width:20px;height:20px;border-radius:50%;background:var(--white)}
.bottom{left:0;top:3391px;width:1200px;height:57px;background:var(--dark)}
.bottom-grad{left:0;top:3391px;width:740px;height:57px;background:linear-gradient(90deg,#9bcb3c 0%,#6fd3a3 60%,rgba(35,35,35,0) 100%);clip-path:polygon(0 0,95% 0,100% 100%,0 100%)}
.copy{left:150px;top:3412px;font-size:9px;color:var(--white);font-weight:600}
.legal{left:906px;top:3412px;font-size:9px;color:var(--white);font-weight:600}
</style>
</head>
<body>

<header>
  <div class="abs hero"><div class="hero-photo" role="img" aria-label="Rows of data center server racks with blue network cabling"></div></div>
  <div class="abs logo"><span class="dot"></span>QORBIL</div>
  <nav class="abs nav">
    <span class="active">Qorbil Difference</span><span>Services</span><span>Resources</span><span>Customer Support</span><span>Contact us</span><span class="login">Login</span>
  </nav>
  <h1 class="abs hero-title">FREEDOM FROM <span>IT</span> WORRIES</h1>
  <p class="abs hero-copy">Your company does not need to buy an expensive equipement, and your data will always be safe and secure at our quality Tier-4 Data centers</p>
  <a class="abs btn btn-fill hero-cta">Contact us</a>
  <a class="abs btn btn-ghost hero-more">Learn more</a>
  <div class="abs slide-dots"><i class="on"></i><i></i><i></i><i></i><i></i></div>
  <div class="abs scroll-down"></div>
</header>

<section>
  <h2 class="abs section-title" style="top:628px">We Make Your IT Secure and Simple</h2>
  <p class="abs section-sub" style="top:678px">Our Best Services</p>

  <article class="abs card" style="left:150px;top:742px">
    <div class="ph" role="img" aria-label="Team working together at laptops" style="background:linear-gradient(135deg,#b89a7a,#6d7f8c)"></div>
    <h3>Freedom from IT Worries</h3>
    <p>Get real time system access for your employees from anywhere at anytime.</p>
    <span class="more">Read More</span>
  </article>
  <article class="abs card" style="left:464px;top:742px">
    <div class="ph" role="img" aria-label="Open plan office full of desks" style="background:linear-gradient(135deg,#3c4148,#8c9096)"></div>
    <h3>Work Securely from Anywhere, Anytime</h3>
    <p>Qorbil's secure IT systems delivered 100% uninterrupted service during all hurricanes and tropical storms, including...</p>
    <span class="more">Read More</span>
  </article>
  <article class="abs card" style="left:779px;top:742px">
    <div class="ph" role="img" aria-label="Help desk staff wearing headsets" style="background:linear-gradient(135deg,#e6e9ec,#9aa7b3)"></div>
    <h3>Houston-based 24/7 Help Desk Support</h3>
    <p>Qorbil provides Live local 24/7 Help Desk and Tier 3 support to Houston area businesses.</p>
    <span class="more">Read More</span>
  </article>
  <article class="abs card" style="left:294px;top:1099px">
    <div class="ph" role="img" aria-label="Server cabinet in a data center" style="background:linear-gradient(135deg,#2d3338,#a4aab0)"></div>
    <h3>Eliminate Unpredictable IT Expenses</h3>
    <p>Your company does not need to buy any expensive equipment, and your data will always be safe at our Tier-4 data centers.</p>
    <span class="more">Read More</span>
  </article>
  <article class="abs card" style="left:634px;top:1099px">
    <div class="ph" role="img" aria-label="Colleagues meeting around a table" style="background:linear-gradient(135deg,#3d4a52,#b07a4e)"></div>
    <h3>Reduce IT Costs</h3>
    <p>Lower your total IT costs with Qorbil's simple flat fee structure so you can focus on growing your business.</p>
    <span class="more">Read More</span>
  </article>
</section>

<div class="abs divider"></div>

<section>
  <h2 class="abs section-title" style="top:1563px">Our success is measured by our client's growth</h2>
  <p class="abs section-sub" style="top:1618px">Happy Clients</p>

  <article class="abs quote" style="left:150px;top:1701px">
    <h4 style="margin-top:8px">BRIGHTFACET</h4>
    <p>"As an e-retailer, our business relies on our computer system. We're no longer bogged down by computer downtime or security threats. With Qorbil, I can focus on growing my business."</p>
    <div class="who"><b>Dario Quent</b>Executive VP</div>
  </article>
  <div class="abs avatar" role="img" aria-label="Client portrait" style="left:178px;top:1684px;background:#8a6a55"></div>

  <article class="abs quote" style="left:595px;top:1701px">
    <h4 style="margin-top:8px">LEDGERLY</h4>
    <p>"Ledgerly began growing so rapidly as we have worked with Qorbil. We've realized new technologies and strategic advantages over the competition, and I never worry about security, backups."</p>
    <div class="who"><b>Mira Tolland</b>President Ledgerly Corp</div>
  </article>
  <div class="abs avatar" role="img" aria-label="Client portrait" style="left:623px;top:1684px;background:#5b6f86"></div>

  <article class="abs quote" style="left:1040px;top:1701px">
    <h4 style="margin-top:8px;color:#999">HARLAN PRUETT</h4>
    <p>"We switched our firm to Qorbil and now work with peace of mind. Our data and every application are always there."</p>
    <div class="who"><b>Harlan J. Pruett</b>CEO PA</div>
  </article>
  <div class="abs avatar" role="img" aria-label="Client portrait" style="left:1068px;top:1684px;background:#a6a6a6"></div>
  <div class="abs fade"></div>
  <div class="abs q-dots"><i></i><i class="on"></i></div>
</section>

<section>
  <div class="abs cost"></div>
  <div class="abs cost-photo" role="img" aria-label="Close-up of server racks with a green tint"></div>
  <h2 class="abs cost-title">Qorbil will cut your IT services Costs</h2>
  <div class="abs cost-copy">
    <p>Lower your total IT costs with Qorbil's simple <span>flat fee structure</span> so you can focus on growing your business.</p>
    <p>Qorbil's Managed IT services can offer an attractive alternative to investing thousands upfront in technology and personnel, allowing you to manage your IT expenditures on predictable monthly basis. Our customers save an average of 30% on capital IT expenditures.....</p>
    <p class="rm">Read more »</p>
  </div>
  <a class="abs btn btn-fill cost-btn">Contact us</a>
</section>

<section>
  <h2 class="abs section-title" style="top:2543px">Who's using Nu|Core®?</h2>
  <p class="abs section-sub" style="top:2592px;font-style:italic">Our Partners</p>
  <div class="abs partners">
    <div><span class="sq"></span>STONE VARLEY</div>
    <div><span class="sq"></span>KEEP BAYOU GREEN</div>
    <div>TALVERO</div>
    <div><span class="sq"></span>COASTMARK</div>
    <div><span class="sq"></span>BRIGHTFACET</div>
    <div><span class="sq"></span>REACH ONWARD</div>
  </div>
</section>

<section>
  <p class="abs ask">Do you have any questions? Feel free to ask from us!</p>
  <div class="abs subscribe"><span class="field">Your Email Here</span><span class="send">Contact Us</span></div>
</section>

<footer>
  <div class="abs footer"></div>
  <div class="abs fcol" style="left:150px">
    <h4>About Us</h4><div class="rule"></div>
    <div class="flogo"><span class="dot"></span>QORBIL</div>
    <p class="ftag">We make your IT Simple and Secure.</p>
    <div class="socials"><i></i><i></i><i></i><i></i><i></i><i></i></div>
  </div>
  <div class="abs fcol" style="left:405px">
    <h4>Qorbil Difference</h4><div class="rule"></div>
    <ul><li>Core Benefits</li><li>Side by Side Comparison</li><li>vs. IT Consultants</li><li>vs. In-house</li><li>vs. Outsourcing</li></ul>
  </div>
  <div class="abs fcol" style="left:662px">
    <h4>Resources</h4><div class="rule"></div>
    <ul><li>Who do</li><li>we help</li><li>Faces</li><li>Testimonials</li><li>Case Studies</li><li>Customer Logos</li></ul>
  </div>
  <div class="abs fcol" style="left:917px">
    <h4>Services</h4><div class="rule"></div>
    <ul><li>Upfront Audit</li><li>Service Types</li><li>Moving to Qorbil System</li><li>Cost Savings</li><li>Performance Tracking</li></ul>
  </div>
  <div class="abs bottom"></div>
  <div class="abs bottom-grad"></div>
  <p class="abs copy">© Copyright 2017. All Rights Reserved</p>
  <p class="abs legal">Terms of Use &nbsp;|&nbsp; Privacy Policy</p>
</footer>

</body>
</html>
```